Tarrowby Mental Health Care for All

A4 flyer & A3 poster promoting a free service for everyone in the community with moderate to high risk of mental health difficulties. It’s a new service being introduced in a rural/remote community. We created two versions- could be front & back on the A4, & 2 different A3 posters. Perhaps a bi-fold with one side For Referrers & the other side For Patients?? We like the content of our drafts but they need to be presented professionally…. Yet, VERY patient friendly with easy to understand text, icons, etc… whatever is recommended. The indigenous artwork I’ve photographed is for background inspiration. It’s bush medicine. We would like to include something that communicates our respect for the traditional owners, elders past, present and emerging. Thank you.

Target Market(s)

Rural, remote people who are in distress and need access to mental health services

Industry/Entity Type

Mental health

Other font styles liked:
• Calibri??

Colors
00AB8E
00BBA5
67D7C9
C6EFE9
E9F9F6

Requirements
Must have
• Free service; all welcome, call 47215903, we will support you
Nice to have
• Simple, easy to follow, communicates confidence and caring
Should not have
• Too much clutter. Too many words.

```html
<!DOCTYPE html>
<html lang="en">
<head>
<meta charset="utf-8">
<title>Tarrowby Mental Health Care for All – Flyers</title>
<link rel="stylesheet" href="https://fonts.googleapis.com/css2?family=Libre+Baskerville:wght@400;700&family=Rubik:wght@500;700&family=Red+Hat+Display:wght@400;500;700&display=swap">
<style>
:root{
  --teal:#00AB8E;
  --teal-2:#00BBA5;
  --teal-3:#67D7C9;
  --mint:#C6EFE9;
  --mint-pale:#E9F9F6;
  --ink:#1d1d1f;
  --text:#2b2b2b;
  --stage:#a9a9a9;
  --serif:"Libre Baskerville", Georgia, serif;
  --pill:"Rubik", Arial, sans-serif;
  --sans:"Red Hat Display", Arial, sans-serif;
}
*{box-sizing:border-box;margin:0;padding:0}
html,body{width:1200px;height:1117px;overflow:hidden}
body{background:var(--stage);position:relative;font-family:var(--sans);color:var(--text)}
.flyer{position:absolute;top:178px;width:538px;height:759px;background:#fff;overflow:hidden}
.flyer--service{left:61px}
.flyer--coordination{left:615px;width:537px}
.flyer__curves{position:absolute;inset:0;width:100%;height:100%}
.flyer__footer{position:absolute;left:0;bottom:0;width:100%;height:180px}
.brand{position:absolute;left:0;right:0;top:42px;text-align:center}
.brand__dot{width:38px;height:38px;border-radius:50%;background:var(--teal);margin:0 auto 10px}
.brand__name{font-family:var(--serif);font-size:14px;color:#1f6b45;line-height:1.25;font-weight:400}
.abs{position:absolute}
.pill{position:absolute;height:28px;background:var(--teal);color:#fff;font-family:var(--pill);font-weight:700;font-size:21px;line-height:28px;text-align:center;border-radius:2px}
.headline{position:absolute;left:0;right:0;top:206px;text-align:center;font-family:var(--serif);font-weight:700;line-height:1.05}
.headline__lead{display:block;font-size:29px;color:var(--ink)}
.headline__main{display:block;font-size:30px;color:var(--teal)}
.lede{font-size:12.5px;line-height:1.25;text-align:center}
.list-title{font-weight:700;font-size:13px;color:var(--ink)}
.checks{list-style:none}
.checks li{position:relative;padding-left:16px;font-size:11.5px;line-height:1.1;margin-bottom:13px}
.checks li svg{position:absolute;left:0;top:2px;width:9px;height:9px}
.body-copy{font-size:11.5px;line-height:1.15}
.art{position:absolute;border-radius:4px}
.callout{position:absolute;left:0;right:0;top:680px;text-align:center;color:#fff;font-weight:700;font-size:15px;line-height:1.1;z-index:2}
.title-block{position:absolute;left:20px;width:230px;top:212px;text-align:center;font-family:var(--serif);font-weight:700;font-size:23px;line-height:1.05;color:var(--teal)}
.steps{position:absolute;left:45px;top:330px;width:230px;list-style:none}
.step{position:relative;height:70px;padding-left:55px}
.step__icon{position:absolute;left:0;top:2px;width:44px;height:44px}
.step__title{font-size:8.5px;font-weight:700;color:var(--teal);margin-bottom:3px}
.step__text{font-size:7.6px;line-height:1.25;color:#333}
.right-col{position:absolute;left:290px;width:200px}
</style>
</head>
<body>

<!-- Service flyer -->
<section class="flyer flyer--service">
  <svg class="flyer__curves" viewBox="0 0 538 759" aria-hidden="true">
    <path d="M0 70 C40 150 130 190 270 186 C140 205 50 190 0 160 Z" fill="var(--mint)"/>
    <path d="M538 50 C525 140 450 190 320 192 C450 185 525 140 538 110 Z" fill="var(--mint)"/>
    <path d="M70 0 C70 140 170 180 268 180 C380 180 470 120 485 0 Z" fill="var(--teal)"/>
    <path d="M135 0 C135 108 200 142 268 142 C340 142 402 100 402 0 Z" fill="#fff"/>
  </svg>
  <div class="brand"><div class="brand__dot"></div><div class="brand__name">Clearwater Minds<br>&amp; Wellbeing</div></div>

  <h1 class="headline"><span class="headline__lead">FULLY FUNDED</span><span class="headline__main">MENTAL HEALTH SERVICE</span></h1>

  <div class="pill" style="left:55px;top:290px;width:176px">Who</div>
  <p class="lede abs" style="left:48px;width:190px;top:329px">For people at risk of moderete severe mental disorders</p>
  <div class="art" role="img" aria-label="Illustration of people fitting puzzle pieces into a large head profile" style="left:56px;top:370px;width:200px;height:280px;background:linear-gradient(160deg,#f6d56a,#f3c640 55%,var(--mint) 100%)"></div>

  <div class="pill" style="left:292px;top:290px;width:201px">What</div>
  <div class="abs" style="left:292px;top:329px;width:215px">
    <p class="list-title" style="margin-bottom:9px">Coordinated care services that:</p>
    <ul class="checks">
      <li><svg viewBox="0 0 10 10"><circle cx="5" cy="5" r="4.3" fill="none" stroke="var(--teal)" stroke-width="1.1"/><path d="M3 5.2l1.4 1.4L7.2 3.7" fill="none" stroke="var(--teal)" stroke-width="1.1"/></svg>employ best practices in risk management + cognitive behavioural therapy</li>
      <li><svg viewBox="0 0 10 10"><circle cx="5" cy="5" r="4.3" fill="none" stroke="var(--teal)" stroke-width="1.1"/><path d="M3 5.2l1.4 1.4L7.2 3.7" fill="none" stroke="var(--teal)" stroke-width="1.1"/></svg>complement, existing mental health services</li>
      <li><svg viewBox="0 0 10 10"><circle cx="5" cy="5" r="4.3" fill="none" stroke="var(--teal)" stroke-width="1.1"/><path d="M3 5.2l1.4 1.4L7.2 3.7" fill="none" stroke="var(--teal)" stroke-width="1.1"/></svg>provide stepped care and needs based distribution of resources</li>
    </ul>
  </div>

  <div class="pill" style="left:292px;top:480px;width:201px">How</div>
  <p class="body-copy abs" style="left:292px;top:521px;width:215px">Upon receiving your referral (Via GP, Self or Other), our reception staff will organise a brief interview to determine eligibility. Please allow 15mins of time for this call.</p>

  <svg class="flyer__footer" viewBox="0 579 538 180" aria-hidden="true">
    <defs>
      <linearGradient id="edgeFadeA" gradientUnits="userSpaceOnUse" x1="0" y1="0" x2="220" y2="0">
        <stop offset="0" stop-color="#fff"/><stop offset="1" stop-color="#fff" stop-opacity="0"/>
      </linearGradient>
    </defs>
    <path d="M0 640 C150 585 390 590 538 648 L538 759 L0 759 Z" fill="var(--mint)"/>
    <path d="M0 705 C110 655 390 615 538 655 L538 759 L0 759 Z" fill="var(--teal)"/>
    <path d="M0 705 C110 655 390 615 538 655" stroke="url(#edgeFadeA)" stroke-width="4" fill="none"/>
  </svg>
  <p class="callout">Please call our friendly reception<br>staff on 4721 5903 to discuss any questions,<br>queries or concerns</p>
</section>

<!-- Coordination flyer -->
<section class="flyer flyer--coordination">
  <svg class="flyer__curves" viewBox="0 0 537 759" aria-hidden="true">
    <path d="M0 70 C40 150 130 190 270 186 C140 205 50 190 0 160 Z" fill="var(--mint)"/>
    <path d="M537 50 C525 140 450 190 320 192 C450 185 525 140 537 110 Z" fill="var(--mint)"/>
    <path d="M70 0 C70 140 170 180 268 180 C380 180 470 120 485 0 Z" fill="var(--teal)"/>
    <path d="M135 0 C135 108 200 142 268 142 C340 142 402 100 402 0 Z" fill="#fff"/>
  </svg>
  <div class="brand"><div class="brand__dot"></div><div class="brand__name">Clearwater Minds<br>&amp; Wellbeing</div></div>

  <h1 class="title-block">Tarrowby<br>P4 Clinical Mental<br>Health Care<br>Coordination</h1>
  <div class="art" role="img" aria-label="Illustration of two clinicians assembling puzzle pieces shaped like a head" style="left:290px;top:185px;width:195px;height:128px;background:linear-gradient(135deg,var(--teal),#0f4a5a 60%,var(--mint))"></div>

  <ol class="steps">
    <li class="step">
      <svg class="step__icon" viewBox="0 0 44 44"><circle cx="22" cy="24" r="19" fill="none" stroke="var(--teal)" stroke-width="2"/><circle cx="8" cy="8" r="7" fill="var(--teal)"/><text x="8" y="11.5" font-size="10" fill="#fff" text-anchor="middle" font-family="Arial">1</text><circle cx="22" cy="20" r="3.5" fill="var(--teal)"/><path d="M15 31c1-5 13-5 14 0z" fill="var(--teal)"/></svg>
      <p class="step__title">Referral Triage</p>
      <p class="step__text">Referral received via GP or Self or other. Eligibility determined through New Service Triage. Form Current GP referral required</p>
    </li>
    <li class="step" style="height:80px">
      <svg class="step__icon" viewBox="0 0 44 44"><circle cx="22" cy="24" r="19" fill="none" stroke="var(--teal)" stroke-width="2"/><circle cx="8" cy="8" r="7" fill="var(--teal)"/><text x="8" y="11.5" font-size="10" fill="#fff" text-anchor="middle" font-family="Arial">2</text><rect x="17" y="13" width="10" height="7" rx="1.5" fill="var(--teal)"/><circle cx="16" cy="26" r="3" fill="var(--teal)"/><circle cx="28" cy="26" r="3" fill="var(--teal)"/><path d="M11 35c1-4 9-4 10 0zM23 35c1-4 9-4 10 0z" fill="var(--teal)"/></svg>
      <p class="step__title">Initial Consultation</p>
      <p class="step__text">Understand consumer's health concerns and goals. Provide information on available services. Assess/Manage safety risks. Facilitate access to appropriate support</p>
    </li>
    <li class="step" style="height:62px">
      <svg class="step__icon" viewBox="0 0 44 44"><circle cx="22" cy="24" r="19" fill="none" stroke="var(--teal)" stroke-width="2"/><circle cx="8" cy="8" r="7" fill="var(--teal)"/><text x="8" y="11.5" font-size="10" fill="#fff" text-anchor="middle" font-family="Arial">3</text><circle cx="24" cy="21" r="6" fill="none" stroke="var(--teal)" stroke-width="2.2"/><path d="M20 25l-6 7" stroke="var(--teal)" stroke-width="2.6"/></svg>
      <p class="step__title">Case conference</p>
      <p class="step__text">Multidisciplinate patient care plan<br>Ensure access to necessary services</p>
    </li>
    <li class="step">
      <svg class="step__icon" viewBox="0 0 44 44"><circle cx="22" cy="24" r="19" fill="none" stroke="var(--teal)" stroke-width="2"/><circle cx="8" cy="8" r="7" fill="var(--teal)"/><text x="8" y="11.5" font-size="10" fill="#fff" text-anchor="middle" font-family="Arial">4</text><rect x="15" y="14" width="13" height="18" rx="1.5" fill="none" stroke="var(--teal)" stroke-width="2"/><path d="M18 20h7M18 24h5" stroke="var(--teal)" stroke-width="1.6"/><circle cx="28" cy="30" r="4" fill="var(--teal)"/></svg>
      <p class="step__title">Case Review and Evaluation</p>
      <p class="step__text">CMW Health Professionals assist, with care implementation. Direct mental health services for complex cases</p>
    </li>
  </ol>

  <div class="pill" style="left:290px;top:335px;width:200px">Who</div>
  <p class="lede right-col" style="top:372px;font-size:9.5px">For consumers with moderate-Severe risk of mental disorder</p>
  <div class="pill" style="left:290px;top:410px;width:200px">What</div>
  <div class="right-col" style="top:449px;width:215px">
    <p class="list-title" style="margin-bottom:9px">Coordinated care services that:</p>
    <ul class="checks">
      <li><svg viewBox="0 0 10 10"><circle cx="5" cy="5" r="4.3" fill="none" stroke="var(--teal)" stroke-width="1.1"/><path d="M3 5.2l1.4 1.4L7.2 3.7" fill="none" stroke="var(--teal)" stroke-width="1.1"/></svg>employ best practices in risk management + cognitive behavioural therapy</li>
      <li><svg viewBox="0 0 10 10"><circle cx="5" cy="5" r="4.3" fill="none" stroke="var(--teal)" stroke-width="1.1"/><path d="M3 5.2l1.4 1.4L7.2 3.7" fill="none" stroke="var(--teal)" stroke-width="1.1"/></svg>complement, existing mental health services</li>
      <li><svg viewBox="0 0 10 10"><circle cx="5" cy="5" r="4.3" fill="none" stroke="var(--teal)" stroke-width="1.1"/><path d="M3 5.2l1.4 1.4L7.2 3.7" fill="none" stroke="var(--teal)" stroke-width="1.1"/></svg>provide stepped care and needs based distribution of resources</li>
    </ul>
  </div>

  <svg class="flyer__footer" viewBox="0 579 537 180" aria-hidden="true">
    <defs>
      <linearGradient id="edgeFadeB" gradientUnits="userSpaceOnUse" x1="0" y1="0" x2="220" y2="0">
        <stop offset="0" stop-color="#fff"/><stop offset="1" stop-color="#fff" stop-opacity="0"/>
      </linearGradient>
    </defs>
    <path d="M0 640 C150 585 390 590 537 648 L537 759 L0 759 Z" fill="var(--mint)"/>
    <path d="M0 705 C110 655 390 615 537 655 L537 759 L0 759 Z" fill="var(--teal)"/>
    <path d="M0 705 C110 655 390 615 537 655" stroke="url(#edgeFadeB)" stroke-width="4" fill="none"/>
  </svg>
  <p class="callout">Please call our friendly reception<br>staff on 4721 5903 to discuss any questions,<br>queries or concerns</p>
</section>

</body>
</html>
```